Equipment Finance Specialist I work with companies who need the funds to buy their equipment

I would like a business card that stands out on the shelves. I want to be able to hand it to someone and say WOW. This card should have my logo.
You can put color into it I am very open on design and color

What my company does is we deal with dealerships that sell equipment such as Dump Trucks garbage trucks tractors trailers. Customers get referred to us and depending on their time in business we will ask for the following items

Companies that have been in business for more than two years we have a credit application program up to 250K . With this program we need the following items Credit application filled out(which is what I would like to be able for the customer to click on my website to get.) as well as three current month bank statements.

Deals over 250k we will need the following items

2 years business tax returns
2 years personal tax returns
Profit & Loss statement
Personal Financial Statement

what we do
100% FINANCING
SEASONAL PAYMENTS
LOAN BALLOON PAYMENTS
TRAC LEASING
LOW-INTEREST REFINANCING RATES
DEBT CONSOLIDATION

We specialize in creative financing solutions and offer a variety of reliable, flexible and expandable lending choices.

Target Market(s)

Trucking Companies

Industry/Entity Type

Trucking Company

Contact Information for Business Card

* $250,000 Application only Program
* Loans from $30,000 to 5,000,000
* Competitive Interest Rates

Font styles to use
Serif
Sans Serif

Colors

Designer to choose colors to be used in the design.

Requirements
Must have
• On the back of the card.
• * $250,000 Application only Program
• * Loans from $30,000 to 5,000,000
• My name, email, website. address
• * Competitive Interest Rates
• * 100% Financing
Nice to have
• I want my logo to pop on the card
• My logo is the great one I would like to use
Should not have
• I am up for your creativity as well

```html
<!DOCTYPE html>
<html lang="en">
<head>
<meta charset="UTF-8">
<title>Summit Lending – Business Card</title>
<link rel="stylesheet" href="https://fonts.googleapis.com/css2?family=Exo+2:wght@700;800&family=Roboto:wght@400;500&display=swap">
<style>
  :root {
    --navy: #1f2d6b;
    --navy-dark: #141d4d;
    --red: #d8252f;
    --orange: #f07a1c;
    --yellow: #e6d92a;
    --white: #ffffff;
    --paper: #f4f5f8;
    --ink: #1f2d6b;
    --steel-dark: #0e0f11;
    --steel-mid: #3a3c40;
    --silver: #d9dadc;
    --backdrop: #8a7356;
  }
  * { margin: 0; padding: 0; box-sizing: border-box; }
  html, body { width: 900px; height: 1200px; overflow: hidden; }
  body {
    position: relative;
    background: var(--backdrop);
    font-family: "Roboto", Arial, sans-serif;
  }
  .card {
    position: absolute;
    left: 88px;
    width: 734px;
    height: 432px;
    border-radius: 22px;
    overflow: hidden;
    box-shadow: 0 10px 24px rgba(0,0,0,.35);
  }

  /* ---------- Front ---------- */
  .card-front { top: 124px; background: linear-gradient(180deg, var(--white) 60%, var(--paper)); }
  .front-top-band {
    position: absolute; left: 0; top: 0; width: 100%; height: 52px;
    background: linear-gradient(180deg, #7d0f14 0%, var(--red) 60%, var(--orange) 85%, var(--yellow) 100%);
  }
  .front-bottom-band {
    position: absolute; left: 0; bottom: 0; width: 100%; height: 50px;
    background: linear-gradient(180deg, #5d6aa8 0%, var(--navy) 30%, var(--navy-dark) 100%);
    display: flex; align-items: center; justify-content: center;
  }
  .website {
    font-family: "Exo 2", Arial, sans-serif; font-weight: 800;
    letter-spacing: 1.5px; font-size: 17px; color: var(--white);
  }
  .holder { position: absolute; left: 47px; top: 108px; }
  .holder-name {
    font-family: "Exo 2", Arial, sans-serif; font-weight: 800;
    font-size: 21px; letter-spacing: 1px; color: var(--navy);
  }
  .holder-title {
    font-family: "Exo 2", Arial, sans-serif; font-weight: 800;
    font-size: 16px; letter-spacing: .5px; color: var(--red); margin-top: 4px;
  }
  .brand {
    position: absolute; display: flex; align-items: center; gap: 12px;
  }
  .brand-mark { border-radius: 50%; flex: none; }
  .brand-name {
    font-family: "Exo 2", Arial, sans-serif; font-weight: 800;
    text-transform: uppercase; line-height: 1; letter-spacing: 1px;
  }
  .brand-front { right: 56px; top: 112px; }
  .brand-front .brand-mark { width: 52px; height: 52px; background: var(--navy); }
  .brand-front .brand-name { font-size: 34px; color: var(--navy); }

  .offers {
    position: absolute; right: 56px; top: 202px; list-style: none; text-align: right;
  }
  .offers li {
    font-size: 17px; font-weight: 500; color: var(--ink); line-height: 23px;
  }
  .offers li::after {
    content: ""; display: inline-block; width: 8px; height: 8px;
    background: var(--red); margin-left: 10px; vertical-align: 1px;
  }
  .divider {
    position: absolute; left: 47px; top: 306px; width: 645px; height: 2px;
    background: linear-gradient(90deg, var(--navy) 0 50%, var(--red) 50% 100%);
  }
  .contacts { position: absolute; left: 47px; top: 320px; list-style: none; }
  .contacts li {
    display: flex; align-items: center; gap: 10px;
    font-size: 17px; color: var(--ink); line-height: 24px;
  }
  .contacts svg { width: 18px; height: 18px; flex: none; }
  .address {
    position: absolute; right: 56px; top: 320px; text-align: right;
    font-style: normal; font-size: 17px; color: var(--ink); line-height: 24px;
  }

  /* ---------- Back ---------- */
  .card-back {
    top: 640px;
    background:
      radial-gradient(ellipse at 50% 45%, #2b2c30 0%, transparent 65%),
      linear-gradient(180deg, var(--steel-dark) 0%, var(--steel-mid) 100%);
  }
  .brand-back { left: 50%; top: 180px; transform: translateX(-50%); }
  .brand-back .brand-mark { width: 64px; height: 64px; background: var(--red); }
  .brand-back .brand-name { font-size: 48px; color: var(--white); white-space: nowrap; }
  .back-band {
    position: absolute; left: 0; top: 378px; width: 100%; height: 28px;
    background: linear-gradient(180deg, #f3f3f4 0%, var(--silver) 50%, #a9abaf 100%);
    border-bottom: 2px solid var(--red);
    display: flex; align-items: center; justify-content: center;
  }
  .back-band .website { color: #1a1a1c; font-size: 16px; }
</style>
</head>
<body>

<section class="card card-front" aria-label="Business card front">
  <div class="front-top-band"></div>

  <div class="holder">
    <p class="holder-name">MARCUS WHITFIELD</p>
    <p class="holder-title">CEO/FOUNDER</p>
  </div>

  <div class="brand brand-front">
    <span class="brand-mark"></span>
    <span class="brand-name">Summit Lending</span>
  </div>

  <ul class="offers">
    <li>$250,000 Application only Program</li>
    <li>Loans from $30,000 to 5,000,000</li>
    <li>Competitive Interest Rates</li>
    <li>100% Financing</li>
  </ul>

  <div class="divider"></div>

  <ul class="contacts">
    <li>
      <svg viewBox="0 0 24 24" aria-hidden="true"><path fill="#d8252f" d="M6.6 10.8a15.2 15.2 0 0 0 6.6 6.6l2.2-2.2c.3-.3.7-.4 1-.2 1.1.4 2.3.6 3.6.6.6 0 1 .4 1 1V20c0 .6-.4 1-1 1A17 17 0 0 1 3 4c0-.6.4-1 1-1h3.5c.6 0 1 .4 1 1 0 1.3.2 2.5.6 3.6.1.3 0 .7-.2 1z"/></svg>
      351-555-014-286
    </li>
    <li>
      <svg viewBox="0 0 24 24" aria-hidden="true"><rect x="2" y="5" width="20" height="14" fill="#d8252f"/><path d="M2 5l10 8 10-8" fill="none" stroke="#fff" stroke-width="1.8"/></svg>
      marcus@summitlending.com
    </li>
  </ul>

  <address class="address">
    Rua das Oliveiras, 148<br>
    4050-262, Porto Central
  </address>

  <div class="front-bottom-band"><span class="website">WWW.SUMMITLENDING.COM</span></div>
</section>

<section class="card card-back" aria-label="Business card back">
  <div class="brand brand-back">
    <span class="brand-mark"></span>
    <span class="brand-name">Summit Lending</span>
  </div>
  <div class="back-band"><span class="website">WWW.SUMMITLENDING.COM</span></div>
</section>

</body>
</html>
```